Letterhead Design Project

Professional but modern letterhead.

Target Market(s)

mining companies

Industry/Entity Type

It Professional

Colors

Designer to choose colors to be used in the design.

```html
<!DOCTYPE html>
<html lang="en">
<head>
<meta charset="utf-8">
<title>Korven Letterhead</title>
<link rel="stylesheet" href="https://fonts.googleapis.com/css2?family=Open+Sans:wght@400;600;700&display=swap">
<style>
  :root {
    --brand-blue: #1c4a97;
    --brand-blue-deep: #143c82;
    --brand-blue-light: #2e62b8;
    --text-grey: #4a4a4a;
    --watermark: #eceef5;
    --paper: #ffffff;
    --backdrop: #e6e7ea;
  }
  * { margin: 0; padding: 0; box-sizing: border-box; }
  html, body {
    width: 1105px;
    height: 1200px;
    overflow: hidden;
    background: var(--backdrop);
    font-family: "Open Sans", Arial, sans-serif;
  }
  .letterhead {
    position: absolute;
    left: 104px;
    top: 20px;
    width: 896px;
    height: 1160px;
    background: var(--paper);
    overflow: hidden;
    box-shadow: 0 2px 10px rgba(0,0,0,0.12);
  }
  .top-band {
    position: absolute;
    left: 0; top: 0;
    width: 100%;
    height: 10px;
    background: var(--brand-blue);
  }
  .brand {
    position: absolute;
    left: 58px;
    top: 104px;
    display: flex;
    align-items: center;
    gap: 12px;
  }
  .brand-dot {
    width: 18px;
    height: 18px;
    border-radius: 50%;
    background: var(--brand-blue);
  }
  .brand-name {
    font-size: 40px;
    font-weight: 600;
    color: var(--brand-blue);
    letter-spacing: 1px;
  }
  .contact {
    position: absolute;
    left: 620px;
    top: 104px;
    font-size: 13px;
    color: var(--text-grey);
    line-height: 19px;
  }
  .contact-item {
    display: flex;
    align-items: center;
    gap: 7px;
  }
  .contact-icon {
    width: 11px;
    height: 11px;
  }
  .contact-address {
    margin-top: 10px;
  }
  .watermark {
    position: absolute;
    left: 0;
    top: 440px;
    width: 100%;
    text-align: center;
    font-size: 150px;
    font-weight: 600;
    color: var(--watermark);
    letter-spacing: 4px;
  }
  .footer-wave {
    position: absolute;
    left: 0;
    bottom: 0;
    width: 896px;
    height: 170px;
  }
  .footer-url {
    position: absolute;
    right: 46px;
    bottom: 30px;
    font-size: 20px;
    font-weight: 700;
    color: var(--paper);
  }
</style>
</head>
<body>
  <main class="letterhead">
    <div class="top-band"></div>

    <header class="brand">
      <span class="brand-dot"></span>
      <span class="brand-name">KORVEN</span>
    </header>

    <address class="contact" style="font-style:normal">
      <div class="contact-item">
        <svg class="contact-icon" viewBox="0 0 12 12"><circle cx="6" cy="6" r="6" fill="#1c4a97"/><path d="M4 3.2l1 1.6-.6.6c.4.9 1 1.5 1.9 1.9l.6-.6 1.6 1-.5 1c-2.4-.3-4.3-2.2-4.6-4.6z" fill="#fff"/></svg>
        <span>415-302-7781</span>
      </div>
      <div class="contact-item">
        <svg class="contact-icon" viewBox="0 0 12 12"><circle cx="6" cy="6" r="6" fill="#1c4a97"/><rect x="4" y="2.6" width="4" height="6.8" rx="0.8" fill="#fff"/></svg>
        <span>415-302-7792</span>
      </div>
      <div class="contact-item">
        <svg class="contact-icon" viewBox="0 0 12 12"><circle cx="6" cy="6" r="6" fill="#1c4a97"/><rect x="3" y="4.5" width="6" height="4" fill="#fff"/><rect x="4" y="2.8" width="4" height="1.5" fill="#fff"/></svg>
        <span>415-302-7803</span>
      </div>
      <div class="contact-item">
        <svg class="contact-icon" viewBox="0 0 12 12"><circle cx="6" cy="6" r="6" fill="#1c4a97"/><rect x="2.8" y="3.8" width="6.4" height="4.4" fill="#fff"/><path d="M2.8 3.8L6 6.4 9.2 3.8" stroke="#1c4a97" stroke-width="0.8" fill="none"/></svg>
        <span>office@korvenit.com</span>
      </div>
      <div class="contact-address">Suite # 410, Ridge Bldg, Co 80214</div>
    </address>

    <div class="watermark" aria-hidden="true">KORVEN</div>

    <svg class="footer-wave" viewBox="0 0 896 170" preserveAspectRatio="none" aria-hidden="true">
      <path d="M0,0 C60,50 200,92 420,92 C620,92 780,78 896,82 L896,170 L0,170 Z" fill="var(--brand-blue-light)"/>
      <path d="M0,30 C120,90 280,110 470,104 C650,98 790,90 896,94" stroke="#ffffff" stroke-width="4" fill="none"/>
      <path d="M0,44 C130,104 290,118 480,112 C660,106 800,100 896,102 L896,170 L0,170 Z" fill="var(--brand-blue-deep)"/>
    </svg>
    <div class="footer-url">www.korvenit.com</div>
  </main>
</body>
</html>
```